Harborline Stay Collective Business Card Design

Design a business card for Harborline Stay Collective. Look at the website for colors and reference. Card should have logo, name, title, office number, mobile number, email, URL and a tagline like, "Luxury Hotel & Resort Email Marketing" (This might change).

https://www.harborlinestaycollective.net

The rest I will leave up to your imagination.

Contact Information for Business Card

Logo, name, title, office number, mobile number, email, URL and a tagline like, "Luxury Hotel & Resort Email Marketing" (This might change).

```html
<!DOCTYPE html>
<html lang="en">
<head>
<meta charset="utf-8">
<title>Harborline Stay Collective – Business Card</title>
<link href="https://fonts.googleapis.com/css2?family=Open+Sans:wght@400;600;700&display=swap" rel="stylesheet">
<style>
  :root {
    --stage: #222222;
    --orange: #f37321;
    --paper: #fdfdf6;
    --ink: #111111;
    --white: #ffffff;
  }
  * { box-sizing: border-box; margin: 0; padding: 0; }
  html, body { width: 1200px; height: 780px; overflow: hidden; }
  body {
    background: var(--stage);
    font-family: "Open Sans", Arial, sans-serif;
    position: relative;
  }
  .card {
    position: absolute;
    top: 235px;
    width: 540px;
    height: 309px;
    overflow: hidden;
  }
  .card--front { left: 40px; background: var(--paper); }
  .card--back { left: 620px; background: var(--orange); }

  .front-wave { position: absolute; inset: 0; }

  .wordmark {
    position: absolute;
    display: flex;
    align-items: center;
    gap: 8px;
    font-weight: 700;
    text-transform: uppercase;
    letter-spacing: 0.04em;
    line-height: 1.1;
  }
  .wordmark__square {
    width: 12px; height: 12px; flex: none;
    background: var(--orange);
  }
  .card--front .wordmark {
    left: 250px; top: 42px;
    font-size: 20px;
    color: var(--ink);
  }
  .card--back .wordmark {
    left: 0; right: 0; top: 50%;
    transform: translateY(-50%);
    justify-content: center;
    font-size: 30px;
    color: var(--white);
    text-align: center;
  }
  .card--back .wordmark__square { width: 18px; height: 18px; background: var(--white); }

  .person { position: absolute; left: 34px; top: 56px; }
  .person__name { font-size: 24px; font-weight: 700; color: var(--ink); line-height: 1.1; }
  .person__first { color: var(--orange); }
  .person__title { font-size: 13px; color: var(--ink); margin-top: 4px; padding-left: 40px; }

  .divider {
    position: absolute; left: 218px; top: 124px;
    width: 2px; height: 78px; background: var(--ink);
  }

  .contacts { position: absolute; left: 234px; top: 124px; list-style: none; }
  .contacts li {
    display: flex; align-items: center; gap: 7px;
    font-size: 13px; color: var(--ink); line-height: 19px;
  }
  .contacts svg { width: 12px; height: 12px; flex: none; }

  .tagline {
    position: absolute; left: 56px; bottom: 16px;
    font-size: 12px; color: var(--white); letter-spacing: 0.02em;
  }
</style>
</head>
<body>

<section class="card card--front" aria-label="Business card front">
  <svg class="front-wave" viewBox="0 0 540 309" preserveAspectRatio="none" aria-hidden="true">
    <path d="M0,212 C40,268 210,292 540,222 L540,309 L0,309 Z" fill="var(--orange)"/>
    <path d="M0,205 C44,256 212,278 540,214 L540,222 C210,292 40,268 0,212 Z" fill="var(--paper)"/>
    <path d="M20,200 C70,258 240,276 500,232" fill="none" stroke="var(--ink)" stroke-width="2.5" stroke-linecap="round"/>
  </svg>

  <div class="wordmark"><span class="wordmark__square"></span><span>Harborline<br>Stay Collective</span></div>

  <div class="person">
    <p class="person__name"><span class="person__first">Marisol</span> Vantreck</p>
    <p class="person__title">Managing Director</p>
  </div>

  <div class="divider"></div>

  <ul class="contacts">
    <li>
      <svg viewBox="0 0 24 24" aria-hidden="true"><path fill="var(--orange)" d="M6.6 10.8a15 15 0 0 0 6.6 6.6l2.2-2.2c.3-.3.7-.4 1-.2 1.1.4 2.3.6 3.6.6.6 0 1 .4 1 1V20c0 .6-.4 1-1 1A17 17 0 0 1 3 4c0-.6.4-1 1-1h3.5c.6 0 1 .4 1 1 0 1.3.2 2.5.6 3.6.1.3 0 .7-.2 1z"/></svg>
      (555) 214-3086
    </li>
    <li>
      <svg viewBox="0 0 24 24" aria-hidden="true"><rect x="6" y="2" width="12" height="20" rx="2" fill="none" stroke="var(--orange)" stroke-width="2"/><circle cx="12" cy="18" r="1.2" fill="var(--orange)"/></svg>
      (555) 478-6120
    </li>
    <li>
      <svg viewBox="0 0 24 24" aria-hidden="true"><circle cx="12" cy="12" r="9" fill="none" stroke="var(--orange)" stroke-width="2"/><path d="M3 12h18M12 3c3 3 3 15 0 18M12 3c-3 3-3 15 0 18" fill="none" stroke="var(--orange)" stroke-width="1.6"/></svg>
      www.harborlinestaycollective.net
    </li>
    <li>
      <svg viewBox="0 0 24 24" aria-hidden="true"><rect x="2" y="5" width="20" height="14" rx="1.5" fill="var(--orange)"/><path d="M3 6l9 7 9-7" fill="none" stroke="var(--paper)" stroke-width="1.8"/></svg>
      info@harborlinestaycollective.net
    </li>
  </ul>

  <p class="tagline">Luxury Hotel &amp; Resort Email Marketing</p>
</section>

<section class="card card--back" aria-label="Business card back">
  <div class="wordmark"><span class="wordmark__square"></span><span>Harborline<br>Stay Collective</span></div>
</section>

</body>
</html>
```